Web Developer Needs a Business Card Design

I need a personal business card design that represents me as a web developer for potential employers. I would like the background to be a dark color on the front for contrast with my logo and name. The back will have all my information along with a smaller version of the logo. I want something with a modern look and feel, not too conservative. This will be used for potential employers and freelance work.

Industry/Entity Type

Business

Contact Information for Business Card

Front should have my logo and name. The back should have all my personal information which would include: name: Tom Varnuch, phone: 570-614-9083, email: tomvarnuch@mailnest.example, website url: www.tomvarnuch.example, logo, web developer.

Font styles to use
Sans Serif

Requirements
Must have
• Must include my logo. The color palette base color will be the logo color.

```html
<!DOCTYPE html>
<html lang="en">
<head>
<meta charset="utf-8">
<title>Tom Varnuch – Business Cards</title>
<link rel="stylesheet" href="https://fonts.googleapis.com/css2?family=Open+Sans:wght@400;600;700&display=swap">
<style>
  :root {
    --stage: #d9d6d2;
    --card-black: #0b0b0b;
    --card-white: #ffffff;
    --teal: #6ccbb5;
    --ink: #141414;
    --light: #f2f2f2;
  }
  * { margin: 0; padding: 0; box-sizing: border-box; }
  html, body {
    width: 1200px;
    height: 913px;
    overflow: hidden;
    background: var(--stage);
    font-family: "Open Sans", Arial, sans-serif;
  }
  .stage { position: relative; width: 1200px; height: 913px; }

  .card {
    position: absolute;
    width: 560px;
    height: 320px;
    border-radius: 16px;
    overflow: hidden;
    background: var(--card-black);
    box-shadow: 0 14px 30px rgba(0,0,0,0.35);
  }
  .card-back { left: 70px; top: 130px; }
  .card-front { left: 570px; top: 460px; }

  .card-shape { position: absolute; inset: 0; width: 100%; height: 100%; }

  /* logo stand-in: plain ring with the name set inside */
  .brand-mark {
    position: absolute;
    display: flex;
    align-items: center;
    justify-content: center;
    border: 10px solid var(--teal);
    border-radius: 50%;
    color: var(--teal);
    font-weight: 700;
    text-align: center;
    line-height: 1.1;
  }
  .card-back .brand-mark {
    left: 62px; top: 62px;
    width: 196px; height: 196px;
    font-size: 25px;
    border-width: 12px;
  }
  .card-front .brand-mark {
    left: 220px; top: 40px;
    width: 120px; height: 120px;
    font-size: 15px;
    border-width: 7px;
  }

  .contact {
    position: absolute;
    right: 26px;
    top: 78px;
    text-align: right;
    color: var(--ink);
  }
  .contact-name {
    font-size: 21px;
    font-weight: 700;
    letter-spacing: 1px;
  }
  .contact-role {
    font-size: 13px;
    font-weight: 600;
    letter-spacing: 1px;
    color: var(--teal);
    margin-bottom: 16px;
  }
  .contact-line {
    display: flex;
    align-items: center;
    justify-content: flex-end;
    gap: 8px;
    font-size: 14px;
    line-height: 23px;
  }
  .contact-line svg { width: 12px; height: 12px; flex: none; }

  .front-name {
    position: absolute;
    left: 0; right: 0;
    top: 186px;
    text-align: center;
    color: var(--light);
    font-size: 30px;
    font-weight: 400;
    letter-spacing: 3px;
  }
  .front-role {
    position: absolute;
    left: 0; right: 0;
    top: 236px;
    text-align: center;
    color: var(--light);
    font-size: 17px;
    letter-spacing: 0.5px;
  }
</style>
</head>
<body>
<main class="stage">

  <section class="card card-back" aria-label="Card back with contact details">
    <svg class="card-shape" viewBox="0 0 560 320" aria-hidden="true">
      <path d="M330,0 C262,8 280,150 240,222 C206,284 140,304 40,320 L560,320 L560,0 Z" fill="var(--teal)"/>
      <path d="M346,0 C280,10 296,154 256,226 C222,288 160,306 70,320 L560,320 L560,0 Z" fill="var(--ink)"/>
      <path d="M352,0 C286,10 302,156 262,228 C228,290 168,308 82,320 L560,320 L560,0 Z" fill="var(--card-white)"/>
    </svg>

    <div class="brand-mark">Tom<br>Varnuch</div>

    <div class="contact">
      <p class="contact-name">TOM VARNUCH</p>
      <p class="contact-role">WEB DEVELOPER</p>
      <p class="contact-line">570-614-9083
        <svg viewBox="0 0 12 12" aria-hidden="true"><path d="M2,1 L4,1 L5,4 L3.5,5 C4.3,6.8 5.2,7.7 7,8.5 L8,7 L11,8 L11,10 C11,10.6 10.6,11 10,11 C5,11 1,7 1,2 C1,1.4 1.4,1 2,1 Z" fill="var(--teal)"/></svg>
      </p>
      <p class="contact-line">tomvarnuch@mailnest.example
        <svg viewBox="0 0 12 12" aria-hidden="true"><rect x="1" y="2.5" width="10" height="7" rx="1" fill="none" stroke="var(--teal)" stroke-width="1.4"/><path d="M1.5,3 L6,6.5 L10.5,3" fill="none" stroke="var(--teal)" stroke-width="1.4"/></svg>
      </p>
      <p class="contact-line">www.tomvarnuch.example
        <svg viewBox="0 0 12 12" aria-hidden="true"><circle cx="6" cy="6" r="5" fill="none" stroke="var(--teal)" stroke-width="1.3"/><ellipse cx="6" cy="6" rx="2.2" ry="5" fill="none" stroke="var(--teal)" stroke-width="1"/><path d="M1,6 H11" stroke="var(--teal)" stroke-width="1"/></svg>
      </p>
    </div>
  </section>

  <section class="card card-front" aria-label="Card front with name">
    <div class="brand-mark">Tom<br>Varnuch</div>
    <p class="front-name">TOM VARNUCH</p>
    <p class="front-role">Front-End Developer</p>
  </section>

</main>
</body>
</html>
```